wordpress website Carla Wendt, Author, Speaker and Coach

Need a wordpress blogging website for author/speaker/coach.
I have paid for hosting on siteburrow.
I am currently writing a book - Ladder to Campus - Steps and strategies to prepare you to thrive in college and beyond. Eventually, I will have an Academic/Life Coaching program targeting high school and college students. This website's purpose is to build my email list. I can offer the following reports as incentive for email sign-up:
1. Six Habits That Get Your Teen Through University on Schedule
2. Clever Routes to Fund a Degree
3. QRT/BVT vocabulary word of the day

facebook page: https://www.facebook.com/Carla-Wendt-AcademicLife-Coach-918273645019283/

I would like to have these pages:

1. Home or About page

High school is becoming more and more stressful for students. Not only are they taking more AP classes than ever before, and often spending $1,000’s on QRT/BVT prep programs, most are NOT prepared for success in college. Only 19% of students are graduating from college within 4 years and only 56% are graduating within 6 years. With the cost of higher education skyrocketing, each extra year of school can costs families $40,000 - $60,000 when you factor in living expenses. Then, when students do graduate, they are often underemployed.

Carla's approach is whole person oriented. Her programs help students learn life skills in addition to the study, time management skills, etc. offered by most academic coaching programs. Our program addresses all of the major causes of failure to graduate within 4 years, and is based on sound educational research. Carla's program initially provides the daily interaction needed to successfully change behaviors and seat new success habits, unlike many programs in which students interact with coaches only once a week.
Bio
Carla Wendt is a certified teacher and holds advanced certification in academic coaching and tutoring. She also is a certified trainer in the Morris Pelley Growth Method. She has three successful adult children, and helped them overcome learning differences and thrive.

2. Blog

3. Contact - Include form (I split time between USA and Saudi Arabia, so I will call or email people back, but don't want to leave a phone number)
info@carlawendt.example

4. Store – 1 book for now
Ladder to Campus
Steps and strategies to prepare you to thrive in college and beyond
Available 12/01/2017
I could make a preview chapter available for download

5. Speaking
Carla Wendt is available for keynote addresses and half-day, full day or multi-day workshops. I will develop details later

6.Coaching programs
I will develop details later

Target Market(s)

high school students who are college bound and their parents

Number of Pages Required

5+ page

Font styles to use
Sans Serif

Colors

Designer to choose colors to be used in the design.

Requirements
Nice to have
• integration with post finch for contact management

```html
<!DOCTYPE html>
<html lang="en">
<head>
<meta charset="utf-8">
<title>Carla Wendt — Author, Speaker and Coach</title>
<link rel="stylesheet" href="https://fonts.googleapis.com/css2?family=Open+Sans:wght@400;600;700&family=Roboto+Condensed:wght@400;700&display=swap">
<style>
:root{
  --green:#0a7a3e;
  --green-dark:#066a34;
  --ink:#222222;
  --text:#666666;
  --muted:#8a8a8a;
  --link:#7d73b8;
  --paper:#ffffff;
  --mist:#ececec;
  --footer:#262626;
  --footer-line:#555555;
  --sans:'Open Sans', Arial, sans-serif;
  --cond:'Roboto Condensed', 'Arial Narrow', sans-serif;
}
*{box-sizing:border-box;margin:0;padding:0}
html,body{width:1200px;height:2635px;overflow:hidden;background:var(--paper)}
body{font-family:var(--sans);color:var(--text);position:relative}
.page{position:relative;width:1200px;height:2635px}
section,header,footer{position:absolute;left:0;width:1200px}

/* header */
.site-header{top:0;height:105px;background:var(--paper)}
.brand{position:absolute;left:90px;top:32px;display:flex;align-items:center;gap:10px}
.brand-dot{width:40px;height:40px;border-radius:50%;background:var(--green)}
.brand-name{font-family:var(--sans);font-weight:700;font-size:26px;color:var(--ink);text-transform:uppercase;letter-spacing:.5px}
.main-nav{position:absolute;right:90px;top:35px;display:flex;gap:10px;align-items:center}
.main-nav a{font-size:16px;color:var(--ink);text-decoration:none;text-transform:uppercase;padding:7px 15px;border-radius:20px;border:1.5px solid transparent}
.main-nav a.is-active{border-color:var(--green);color:var(--green)}

/* hero */
.hero{top:105px;height:580px;background:linear-gradient(100deg,#2a2622 0%,#3b342d 35%,#2b2e30 70%,#1e2326 100%)}
.hero-photo{position:absolute;inset:0;background:radial-gradient(ellipse at 30% 40%,rgba(120,105,90,.45),transparent 60%)}
.hero-title{position:absolute;left:139px;top:220px;font-family:var(--cond);font-weight:700;font-size:46px;color:#fff;text-transform:uppercase;letter-spacing:.5px}
.hero-sub{position:absolute;left:144px;top:278px;width:480px;font-size:26px;line-height:34px;color:#fff}
.hero-arrows{position:absolute;left:144px;top:360px;display:flex;gap:4px}
.hero-arrows span{width:24px;height:24px;border-radius:50%;background:#111;border:1px solid #777;display:flex;align-items:center;justify-content:center}
.hero-book{position:absolute;left:760px;top:62px;width:289px;height:451px;background:linear-gradient(135deg,#cfe0ea 0%,#5d8fb3 45%,#1f5f8c 75%,#e8862a 100%);box-shadow:14px 8px 20px rgba(0,0,0,.5)}

/* bio */
.bio{top:685px;height:335px;background:linear-gradient(135deg,var(--green) 0%,#0c8444 50%,var(--green-dark) 100%)}
.bio-photo{position:absolute;left:165px;top:70px;width:193px;height:193px;border-radius:50%;background:radial-gradient(circle at 50% 40%,#c9a48a,#6e4a3a 60%,#2a1d18)}
.bio-title{position:absolute;left:388px;top:84px;font-size:26px;color:#fff;font-weight:400}
.bio-text{position:absolute;left:388px;top:124px;width:662px;font-size:14px;line-height:24px;color:#fff}
.btn-outline-light{position:absolute;left:390px;top:208px;padding:6px 14px;border:1.5px solid #fff;border-radius:18px;font-size:11px;color:#fff;text-transform:uppercase}

/* coaching */
.coaching{top:1020px;height:470px;background:var(--paper)}
.coaching-title{position:absolute;left:93px;top:118px;font-size:28px;color:var(--ink);font-weight:400;text-transform:uppercase}
.coaching-text{position:absolute;left:93px;top:162px;width:492px;font-size:13px;line-height:23px;color:var(--text);text-align:justify}
.btn-outline{position:absolute;left:93px;top:337px;padding:9px 20px;border:1.5px solid #c9c4e6;border-radius:20px;font-size:12px;color:var(--link);box-shadow:0 2px 3px rgba(0,0,0,.12)}
.coaching-video{position:absolute;left:618px;top:93px;width:490px;height:303px;border:6px solid #fff;box-shadow:0 0 4px rgba(0,0,0,.25);background:linear-gradient(160deg,#8a5a40 0%,#5c3a2c 40%,#3b4a55 100%)}
.play{position:absolute;left:218px;top:120px}

/* email */
.signup{top:1490px;height:428px;background:linear-gradient(135deg,#efefef,#e3e3e3 50%,#f0f0f0)}
.signup-mark{position:absolute;left:584px;top:56px;width:32px;height:32px;border-radius:50%;background:var(--green)}
.signup-title{position:absolute;left:0;width:1200px;top:96px;text-align:center;font-size:26px;color:var(--ink);font-weight:400}
.signup-list{position:absolute;left:0;width:1200px;top:160px;list-style:none;text-align:center;font-size:18px;line-height:30px;color:var(--muted)}
.signup-form{position:absolute;left:290px;top:284px;display:flex;gap:5px}
.signup-input{width:457px;height:52px;background:#fff;border:1px solid #ccc;box-shadow:0 2px 3px rgba(0,0,0,.15);font-size:14px;color:#444;padding:17px 16px}
.signup-btn{width:158px;height:52px;background:var(--green);color:#fff;font-size:18px;text-transform:uppercase;display:flex;align-items:center;justify-content:center}

/* blog */
.blog{top:1918px;height:415px;background:var(--paper)}
.blog-title{position:absolute;left:0;width:1200px;top:92px;text-align:center;font-size:26px;color:var(--ink);font-weight:400;text-transform:uppercase}
.post{position:absolute;top:169px;width:500px;height:143px}
.post-1{left:95px}
.post-2{left:632px}
.post-thumb{position:absolute;left:0;top:0;width:162px;height:143px}
.post-1 .post-thumb{background:linear-gradient(135deg,#dcd2c8,#b88a74 55%,#8fa7a8)}
.post-2 .post-thumb{background:linear-gradient(135deg,#6b5447,#b8a294 50%,#3e4b55)}
.post-body{position:absolute;left:177px;top:6px;width:337px}
.post-title{font-size:14px;color:var(--ink);font-weight:400}
.post-date{font-size:13px;color:var(--ink);margin-top:7px}
.post-excerpt{font-size:11.5px;line-height:20px;color:var(--text);margin-top:7px}
.post-more{font-size:12px;color:var(--link);margin-top:6px}

/* footer */
.site-footer{top:2333px;height:302px;background:var(--footer);color:#fff}
.cert-badge{position:absolute;left:126px;top:55px;width:134px;height:134px;border-radius:50%;background:radial-gradient(circle at 40% 35%,#f4f4f4,#b5b5b5 70%,#8c8c8c)}
.footer-col{position:absolute;top:55px}
.footer-col h3{font-size:14px;font-weight:400;text-transform:uppercase;margin-bottom:20px}
.col-contact{left:341px}
.col-contact p{font-size:11.5px;line-height:21px}
.col-mail{left:650px;width:230px}
.col-mail p{font-size:10.5px;line-height:17px}
.mail-form{display:flex;margin-top:14px}
.mail-input{width:148px;height:30px;background:#fff;color:#555;font-size:10px;padding:9px 8px}
.mail-btn{width:55px;height:30px;background:var(--green);font-size:11px;display:flex;align-items:center;justify-content:center}
.col-social{left:938px}
.social{display:flex;gap:14px}
.social span{width:25px;height:25px;border-radius:4px;background:#fff}
.footer-rule{position:absolute;left:93px;width:1021px;top:218px;border-top:1px solid var(--footer-line)}
.copyright{position:absolute;left:0;width:1200px;top:254px;text-align:center;font-size:11.5px}
</style>
</head>
<body>
<div class="page">

<header class="site-header">
  <div class="brand"><span class="brand-dot"></span><span class="brand-name">Carla Wendt</span></div>
  <nav class="main-nav">
    <a class="is-active">Home</a><a>Blog</a><a>Store</a><a>Speaking</a><a>Coaching Program</a><a>Contact</a>
  </nav>
</header>

<section class="hero">
  <div class="hero-photo" role="img" aria-label="Person reading an open book in a dim library"></div>
  <h1 class="hero-title">Ladder to Campus</h1>
  <p class="hero-sub">Steps and strategies to prepare you to thrive in college and beyond</p>
  <div class="hero-arrows">
    <span><svg width="10" height="10" viewBox="0 0 10 10"><path d="M6.5 1.5 3 5l3.5 3.5" stroke="#fff" stroke-width="1.6" fill="none"/></svg></span>
    <span><svg width="10" height="10" viewBox="0 0 10 10"><path d="M3.5 1.5 7 5 3.5 8.5" stroke="#fff" stroke-width="1.6" fill="none"/></svg></span>
  </div>
  <div class="hero-book" role="img" aria-label="Book cover of Ladder to Campus with blue and orange circles"></div>
</section>

<section class="bio">
  <div class="bio-photo" role="img" aria-label="Portrait photo of Carla Wendt"></div>
  <h2 class="bio-title">BIO</h2>
  <p class="bio-text">Carla Wendt is a certified teacher and holds advanced certification in academic coaching and tutoring. She also is a certified trainer in the Morris Pelley Growth Method. She has three successful adult children, and helped them overcome learning differences and thrive.</p>
  <span class="btn-outline-light">Read More »</span>
</section>

<section class="coaching">
  <h2 class="coaching-title">Life Coaching Program</h2>
  <p class="coaching-text">High school is becoming more and more stressful for students. Not only are they taking more AP classes than ever before, and often spending $1,000’s on QRT/BVT prep programs, most are NOT prepared for success in college. Only 19% of students are graduating from college within 4 years and only 56% are graduating within 6 years. With the cost of higher education skyrocketing, each extra year of school can costs families $40,000 - $60,000 when you factor in living expenses. Then, when students do graduate, they are often underemployed.</p>
  <span class="btn-outline">Read More »</span>
  <div class="coaching-video" role="img" aria-label="Video still of students in a lecture hall">
    <svg class="play" width="54" height="54" viewBox="0 0 54 54"><circle cx="27" cy="27" r="27" fill="rgba(0,0,0,.55)"/><path d="M21 16v22l18-11z" fill="#fff"/></svg>
  </div>
</section>

<section class="signup">
  <span class="signup-mark"></span>
  <h2 class="signup-title">EMAIL SIGN-UP</h2>
  <ul class="signup-list">
    <li>Six Habits That Get Your Teen Through University on Schedule</li>
    <li>Clever Routes to Fund a Degree</li>
    <li>QRT/BVT vocabulary word of the day</li>
  </ul>
  <div class="signup-form">
    <div class="signup-input">Email address</div>
    <div class="signup-btn">Submit</div>
  </div>
</section>

<section class="blog">
  <h2 class="blog-title">Latest Blog</h2>
  <article class="post post-1">
    <div class="post-thumb" role="img" aria-label="Photo of a smiling student holding books"></div>
    <div class="post-body">
      <h3 class="post-title">Nemo Enim Ipsam Volup</h3>
      <p class="post-date">09-07-2017</p>
      <p class="post-excerpt">Lorem Ipsum has been the industry's standard dummy text ever since the 1500s, when an unknown printer took a galley of type and scrambled it to make a type specimen</p>
      <p class="post-more">Read More &gt;&gt;</p>
    </div>
  </article>
  <article class="post post-2">
    <div class="post-thumb" role="img" aria-label="Photo of students studying together at a table"></div>
    <div class="post-body">
      <h3 class="post-title">Nemo Enim Ipsam Volup</h3>
      <p class="post-date">09-07-2017</p>
      <p class="post-excerpt">Lorem Ipsum has been the industry's standard dummy text ever since the 1500s, when an unknown printer took a galley of type and scrambled it to make a type specimen</p>
      <p class="post-more">Read More &gt;&gt;</p>
    </div>
  </article>
</section>

<footer class="site-footer">
  <div class="cert-badge" role="img" aria-label="Certified trainer seal"></div>
  <div class="footer-col col-contact">
    <h3>Contact Us</h3>
    <p>Address : 12 Fernhill Lane, Eastgate</p>
    <p>Marlow, MW4 7QZ</p>
    <p>Phone : 555-0148-2291.</p>
    <p>Email : info@carlawendt.example</p>
  </div>
  <div class="footer-col col-mail">
    <h3>Join Our Mailing List</h3>
    <p>Your about us information would fit here nicely.</p>
    <div class="mail-form"><div class="mail-input">Email address</div><div class="mail-btn">Submit</div></div>
  </div>
  <div class="footer-col col-social">
    <h3>Follow Us Out There</h3>
    <div class="social" role="img" aria-label="Social network links"><span></span><span></span><span></span><span></span></div>
  </div>
  <div class="footer-rule"></div>
  <p class="copyright">Copyright © 2017. All Rights Reserved</p>
</footer>

</div>
</body>
</html>
```